Wine label for family vineyard start-up

Brand new family vineyard needs a new label:

The information we need on the label is the following:
- Merlot & Cabernet (variety)
- Colle Vallarosa (location)
- 2016 (vintage)

The style of the label should be graphic / minimal / masculine.

This is a wine made by three 35yr old guys

Target Market(s)

young & urban

Industry/Entity Type

Vineyard

Logo Text

Merlot & Cabernet / Colle Vallarosa / 2016

Font styles to use
Sans Serif

Requirements
Must have
• clearly legible
• aesthetically pleasing [minimalist]
• sans serif

```html
<!DOCTYPE html>
<html lang="en">
<head>
<meta charset="utf-8">
<title>Colle Vallarosa – Merlot &amp; Cabernet 2016</title>
<link rel="stylesheet" href="https://fonts.googleapis.com/css2?family=Josefin+Sans:wght@400;500;600&display=swap">
<style>
  :root {
    --paper: #ffffff;
    --ink: #1c1c1c;
  }
  html, body {
    margin: 0;
    padding: 0;
    overflow: hidden;
    background: var(--paper);
  }
  .label {
    position: relative;
    width: 1200px;
    height: 720px;
    background: var(--paper);
    color: var(--ink);
    font-family: "Josefin Sans", sans-serif;
    overflow: hidden;
  }
  .label__line {
    position: absolute;
    left: -11px;
    width: 100%;
    margin: 0;
    text-align: center;
    line-height: 1;
    text-transform: uppercase;
    white-space: nowrap;
  }
  .label__estate {
    top: 282px;
    font-size: 77px;
    font-weight: 600;
    letter-spacing: 3px;
    padding-left: 3px;
  }
  .label__variety {
    top: 377px;
    font-size: 44px;
    font-weight: 500;
    letter-spacing: 12px;
    padding-left: 12px;
  }
  .label__vintage {
    top: 455px;
    font-size: 48px;
    font-weight: 500;
    letter-spacing: 6px;
    padding-left: 6px;
  }
</style>
</head>
<body>
  <main class="label">
    <h1 class="label__line label__estate">Colle Vallarosa</h1>
    <p class="label__line label__variety">Merlot &amp; Cabernet</p>
    <p class="label__line label__vintage">2016</p>
  </main>
</body>
</html>
```